DORIVAN
POWER THE FUTURE
Professional
Tobin Rasquelle
2417 Fennimore Lane
Calder Springs, MD 20999
tobin@dorivan7.com
www.dorivan7.com
I can provide logo as need it.
Logo and write this underneath the logo or where you think it will look better.
Have fun!!

```html
<!DOCTYPE html>
<html lang="en">
<head>
<meta charset="utf-8">
<title>DORIVAN Stationery</title>
<link href="https://fonts.googleapis.com/css2?family=Open+Sans:wght@400;600;800&display=swap" rel="stylesheet">
<style>
:root{
  --bg:#e6e8ec;
  --paper:#f7f8fa;
  --blue:#3d6fc4;
  --blue-dark:#2f5aa6;
  --blue-light:#5b8ad6;
  --ink:#5a6170;
  --ink-soft:#8a909c;
  --rule:#c9ced8;
}
*{box-sizing:border-box;margin:0;padding:0}
html,body{width:1200px;height:1011px;overflow:hidden}
body{background:var(--bg);font-family:"Open Sans",Arial,sans-serif;color:var(--ink);position:relative}
.sheet{position:absolute;background:var(--paper);box-shadow:0 6px 18px rgba(0,0,0,.18);overflow:hidden}
.logo{display:flex;flex-direction:column;align-items:center;color:#fff}
.logo-row{display:flex;align-items:center;gap:8px}
.logo-mark{width:12px;height:12px;border-radius:50%;background:#fff}
.logo-name{font-weight:800;letter-spacing:2px;line-height:1}
.logo-tag{font-weight:600;letter-spacing:3px;margin-top:5px;opacity:.9}
.contact{display:flex;align-items:center;gap:5px;white-space:nowrap}
.contact svg{width:10px;height:10px;fill:var(--blue);flex:none}

/* letterhead */
.letterhead{left:60px;top:90px;width:560px;height:792px}
.letterhead-band{height:120px;background:linear-gradient(180deg,var(--blue-light),var(--blue));border-bottom:6px solid var(--blue-dark);display:flex;align-items:center;justify-content:center}
.letterhead-band .logo-name{font-size:34px}
.letterhead-band .logo-tag{font-size:10px}
.letterhead-footer{position:absolute;left:36px;right:36px;bottom:30px;border-top:1px solid var(--rule);padding-top:10px;display:flex;justify-content:space-between;font-size:8.5px;color:var(--ink-soft)}

/* envelope */
.envelope{left:670px;top:90px;width:480px;height:230px}
.envelope-band{height:78px;background:linear-gradient(180deg,var(--blue-light),var(--blue));display:flex;align-items:center;padding-left:26px}
.envelope-band .logo{align-items:flex-start}
.envelope-band .logo-name{font-size:24px}
.envelope-band .logo-tag{font-size:7.5px}
.envelope-address{position:absolute;left:26px;bottom:22px;font-size:9px;color:var(--ink-soft);border-top:1px solid var(--rule);padding-top:8px;width:250px}

/* business cards */
.card{width:400px;height:228px}
.card-back{left:670px;top:372px;background:linear-gradient(160deg,var(--blue-light),var(--blue-dark));display:flex;align-items:center;justify-content:center}
.card-back .logo-name{font-size:32px}
.card-back .logo-tag{font-size:9px}
.card-front{left:670px;top:650px}
.card-front-band{height:74px;background:linear-gradient(180deg,var(--blue-light),var(--blue));display:flex;align-items:center;justify-content:center}
.card-front-band .logo-name{font-size:22px}
.card-front-band .logo-tag{font-size:7px}
.card-name{text-align:center;color:var(--blue);font-size:20px;font-weight:400;margin-top:18px}
.card-rule{width:240px;margin:8px auto 10px;border-top:1px solid var(--rule)}
.card-details{display:grid;grid-template-columns:auto auto;justify-content:center;gap:6px 18px;font-size:9px;color:var(--ink)}
</style>
</head>
<body>
<svg width="0" height="0" style="position:absolute">
  <symbol id="icon-pin" viewBox="0 0 10 10"><path d="M5 0a3.5 3.5 0 0 0-3.5 3.5C1.5 6 5 10 5 10s3.5-4 3.5-6.5A3.5 3.5 0 0 0 5 0zm0 5a1.5 1.5 0 1 1 0-3 1.5 1.5 0 0 1 0 3z"/></symbol>
  <symbol id="icon-phone" viewBox="0 0 10 10"><path d="M2 0.5l2 2-1 1.2c.6 1.3 1.6 2.3 2.9 2.9L7 5.5l2 2-1.3 1.8C4 9 1 6 .7 1.8z"/></symbol>
  <symbol id="icon-mail" viewBox="0 0 10 10"><path d="M0 2h10v6H0zm1 1l4 3 4-3v-.2H1z"/></symbol>
  <symbol id="icon-web" viewBox="0 0 10 10"><circle cx="5" cy="5" r="4.5"/></symbol>
</svg>

<section class="sheet letterhead">
  <header class="letterhead-band">
    <div class="logo"><div class="logo-row"><span class="logo-mark"></span><span class="logo-name">DORIVAN</span></div><span class="logo-tag">POWER THE FUTURE</span></div>
  </header>
  <footer class="letterhead-footer">
    <span class="contact"><svg><use href="#icon-phone"/></svg>1 (410) 555-0182</span>
    <span class="contact"><svg><use href="#icon-pin"/></svg>2417 Fennimore Lane, Calder Springs, MD 20999</span>
    <span class="contact"><svg><use href="#icon-mail"/></svg>tobin@dorivan7.com</span>
    <span class="contact"><svg><use href="#icon-web"/></svg>www.dorivan7.com</span>
  </footer>
</section>

<section class="sheet envelope">
  <header class="envelope-band">
    <div class="logo"><div class="logo-row"><span class="logo-mark"></span><span class="logo-name">DORIVAN</span></div><span class="logo-tag">POWER THE FUTURE</span></div>
  </header>
  <p class="envelope-address contact"><svg><use href="#icon-pin"/></svg>2417 Fennimore Lane, Calder Springs, MD 20999</p>
</section>

<section class="sheet card card-back">
  <div class="logo"><div class="logo-row"><span class="logo-mark"></span><span class="logo-name">DORIVAN</span></div><span class="logo-tag">POWER THE FUTURE</span></div>
</section>

<section class="sheet card card-front">
  <header class="card-front-band">
    <div class="logo"><div class="logo-row"><span class="logo-mark"></span><span class="logo-name">DORIVAN</span></div><span class="logo-tag">POWER THE FUTURE</span></div>
  </header>
  <h1 class="card-name">Tobin Rasquelle</h1>
  <div class="card-rule"></div>
  <div class="card-details">
    <span class="contact"><svg><use href="#icon-phone"/></svg>1 (410) 555-0182</span>
    <span class="contact"><svg><use href="#icon-pin"/></svg>2417 Fennimore Lane, Calder Springs, MD 20999</span>
    <span class="contact"><svg><use href="#icon-phone"/></svg>410-555-0146</span>
    <span class="contact"><svg><use href="#icon-mail"/></svg>tobin@dorivan7.com</span>
    <span class="contact"><svg><use href="#icon-phone"/></svg>410-555-0173</span>
    <span class="contact"><svg><use href="#icon-web"/></svg>www.dorivan7.com</span>
  </div>
</section>
</body>
</html>
```